Brand Business Card for Hotel Cloud Management System

Hello designers,
we are looking for a new brand business card for our product Roomvanta. Our brand Roomvanta is a hotel management system for small hotels, B&B, guesthouses etc. and just recently we are expanding our offer to other European markets. Therefore we need a business card that will communicate not only to the end-users (hoteliers) but also to potential business partners/ We would like the brand business card to be professional looking, but not too serius, modern, elegant, clean, Our brand color is orange, dark grey and it would be nice to see both combined.

Please visit our website www.roomvanta-example.eu to get more impression on what our brand roomvanta stands for.

Please find attached roomvanta logo.

Target Market(s)

small hotels, hoteliers, B&B owners, potential business partners

Industry/Entity Type

Software Service

Contact Information for Business Card

Roomvanta
- hotel software solutions - web booking engine - multi channel manager
www.roomvanta-example.eu
T: +38614007300
E: info@roomvanta-example.net

Font styles to use
Serif
Sans Serif

Colors
f37122
aaaaaa
606060
f6f6f6

Requirements
Must have
• Logo of the brand
• the layout of the business card should be in connection with the look and feel of the website roomvanta-example.eu and logo roomvanta;

```html
<!DOCTYPE html>
<html lang="en">
<head>
<meta charset="utf-8">
<title>Roomvanta Business Card</title>
<link href="https://fonts.googleapis.com/css2?family=Roboto:wght@400;500;700&display=swap" rel="stylesheet">
<style>
  :root {
    --brand-orange: #f37122;
    --ink-dark: #1e1e1e;
    --ink-body: #4a4a4a;
    --card-paper: #f4f4f4;
    --star-tint: #f6ddd0;
    --backdrop: #2b2b2b;
  }
  * { margin: 0; padding: 0; box-sizing: border-box; }
  html, body {
    width: 1200px;
    height: 960px;
    overflow: hidden;
  }
  body {
    position: relative;
    background: var(--backdrop);
    font-family: "Roboto", Arial, sans-serif;
  }
  .card {
    position: absolute;
    width: 600px;
    height: 343px;
    border-radius: 24px;
    background: var(--card-paper);
    overflow: hidden;
    text-align: center;
  }
  .card--front { left: 314px; top: 113px; }
  .card--back  { left: 311px; top: 472px; }

  .star-pattern {
    position: absolute;
    inset: 0;
    background:
      radial-gradient(ellipse at 10% 80%, var(--star-tint) 0%, transparent 30%),
      radial-gradient(ellipse at 90% 15%, var(--star-tint) 0%, transparent 30%),
      radial-gradient(ellipse at 50% 50%, rgba(246,221,208,0.35) 0%, transparent 70%);
    opacity: 0.8;
  }
  .contact-block {
    position: absolute;
    left: 0; right: 0;
    top: 116px;
  }
  .person-name {
    color: var(--brand-orange);
    font-size: 23px;
    font-weight: 700;
    line-height: 26px;
  }
  .person-role {
    color: var(--ink-dark);
    font-size: 15px;
    font-weight: 500;
    line-height: 20px;
  }
  .divider {
    width: 32px;
    height: 2px;
    background: var(--brand-orange);
    margin: 12px auto 12px;
  }
  .contact-line {
    color: var(--ink-body);
    font-size: 14.5px;
    line-height: 19px;
  }

  .brand-lockup {
    position: absolute;
    left: 0; right: 0;
    top: 170px;
  }
  .brand-name {
    color: var(--ink-dark);
    font-size: 50px;
    font-weight: 700;
    line-height: 56px;
    letter-spacing: -0.5px;
  }
  .brand-tagline {
    color: var(--ink-dark);
    font-size: 15px;
    line-height: 20px;
    margin-top: 0;
  }
  .service-list {
    position: absolute;
    left: 0; right: 0;
    top: 294px;
    color: var(--ink-body);
    font-size: 14.5px;
    line-height: 20px;
  }
  .service-dot {
    display: inline-block;
    width: 6px;
    height: 6px;
    border-radius: 50%;
    background: var(--brand-orange);
    margin: 0 2px 1px 2px;
    vertical-align: middle;
  }
</style>
</head>
<body>
  <section class="card card--front">
    <div class="star-pattern" role="img" aria-label="Faint scattered orange star pattern across the card background"></div>
    <div class="contact-block">
      <p class="person-name">Luka Zorman</p>
      <p class="person-role">CEO/Founder</p>
      <div class="divider"></div>
      <p class="contact-line">+38614007300</p>
      <p class="contact-line">info@roomvanta-example.net</p>
      <p class="contact-line">www.roomvanta-example.eu</p>
    </div>
  </section>

  <section class="card card--back">
    <div class="brand-lockup">
      <p class="brand-name">Roomvanta</p>
      <p class="brand-tagline">hotel pms service</p>
    </div>
    <p class="service-list">hotel software solutions<span class="service-dot"></span>web booking engine<span class="service-dot"></span>multi channel manager</p>
  </section>
</body>
</html>
```